Clean, Corporate redesign of existing website

We require a clean corporate professional redesign of our existing poor website, although a simple and elegant structure is required we would like the designer to concentrate on the little things and finishes to give the site a highly professional feel.
The company have supplied the following websites as to use as inspiration http://www.dorvalestone.example/ they like the clean, professional feel of the website
and the fact that the website captures the feel of their industry. Another clean and professional site they liked the look of was http://www.brisklyseafare.example.co.uk/ .
Another inspirational (page level only) http://www.halvertonexpohall.example/thefacilities/floor-maps-and-specifications/ we like the top image and the corporate feel the images give. Auto cad drawings as images or a search for electrical services will fetch up a good selection of images to use as placeholders
A full brief, logos, images etc have been supplied
update: the sector is industrial electrical services, so more towards factory switches and equipement, not domestic light-bulbs etc this is important when choosing images for the site.
Updates
Thank you all for your designs, i will be presenting the best to the company tomorrow who will pick the design that suits so please get any remaining designs to me by tomorrow morning (GMT time) at the latest to be included in the presentation.
Target Market(s)
Business owners and CEO'S
Industry/Entity Type
Electrical
Look and feel

```html
<!DOCTYPE html>
<html lang="en">
<head>
<meta charset="utf-8">
<title>Fenwold Electrical Services Limited</title>
<link href="https://fonts.googleapis.com/css2?family=PT+Sans:wght@400;700&family=Source+Sans+3:wght@400;600;700&display=swap" rel="stylesheet">
<style>
:root{
  --red:#c8101a;
  --red-dark:#a8060f;
  --red-band:#c40f17;
  --ink:#1e1e1e;
  --grey:#555;
  --nav-active:#4a4a4a;
  --band-grey:#e4e4e4;
  --white:#fff;
}
*{margin:0;padding:0;box-sizing:border-box}
html,body{width:916px;height:1200px;overflow:hidden;background:var(--white)}
body{position:relative;font-family:"Source Sans 3",sans-serif;color:var(--ink)}
.abs{position:absolute}
.logo{left:70px;top:46px;color:var(--red-dark);font-family:"PT Sans",sans-serif;font-weight:400;line-height:1}
.logo .name{font-size:30px;letter-spacing:-0.5px}
.logo .sub{font-size:15.5px;letter-spacing:3.2px;margin-top:2px}
.nav{left:297px;top:54px;width:547px;height:43px;background:linear-gradient(#d8141d,#b80a12);border-radius:3px;display:flex;align-items:center;padding:0 4px}
.nav a{color:var(--white);text-decoration:none;font-family:"PT Sans",sans-serif;font-weight:700;font-size:17px;padding:0 16px;height:35px;line-height:35px}
.nav a.active{background:var(--nav-active);margin-right:10px}
.nav a+a{margin-left:4px}
.grey-band{left:0;top:314px;width:916px;height:126px;background:linear-gradient(var(--band-grey),#f7f7f7)}
.hero{left:72px;top:109px;width:772px;height:329px;background:linear-gradient(100deg,#2b5aa8 0%,#c99a80 30%,#9a8e80 55%,#d7d7d2 80%,#b8bcbf 100%)}
.arrow{top:226px;width:54px;height:86px;background:rgba(255,255,255,.92)}
.arrow.left{left:72px;border-radius:0 43px 43px 0}
.arrow.right{left:790px;border-radius:43px 0 0 43px}
.caption{left:85px;top:338px;width:270px;height:86px;background:rgba(30,30,30,.82);padding:10px 14px}
.caption h2{font-family:"PT Sans",sans-serif;font-weight:400;font-size:24px;color:var(--white);letter-spacing:-.3px}
.caption h2 span{color:var(--red)}
.caption p{font-family:"PT Sans",sans-serif;font-size:15px;color:var(--white);margin-top:6px}
.caption p b{color:var(--red);font-weight:400}
.sec-title{font-family:"PT Sans",sans-serif;font-size:17px;color:var(--red)}
.photo{background:linear-gradient(135deg,#cfd1d0,#8b8f92 60%,#d9dbda)}
.lead{left:72px;top:668px;width:448px;font-size:12.5px;font-weight:600;line-height:16px;text-align:justify}
.lead span{color:var(--red)}
.body-text{font-size:10px;line-height:15.5px;color:#333;letter-spacing:-.2px}
.list{left:566px;top:728px;list-style:none;font-size:12px;line-height:19.5px;color:var(--red)}
.read{font-size:11px;font-weight:700;letter-spacing:-.3px;color:var(--ink)}
.band{left:0;top:840px;width:916px;height:257px;background:linear-gradient(var(--red),var(--red-band))}
.overview{left:72px;top:861px;font-family:"PT Sans",sans-serif;font-weight:700;font-size:16px;color:var(--white)}
.tile{top:892px;width:160px;height:103px;border:3px solid var(--white)}
.tile .label{position:absolute;left:0;bottom:14px;background:var(--red);color:var(--white);font-size:12px;font-weight:700;padding:2px 12px;line-height:14px}
.news{left:105px;top:1014px;width:703px;height:50px;background:linear-gradient(#fafafa,#e2e2e2);border:2px solid #ddd;border-radius:3px}
.news .title{position:absolute;left:14px;top:14px;font-size:13px;font-weight:700;color:var(--red)}
.news .title small{font-size:8.5px;color:#444;font-weight:400;margin-left:4px}
.news .signin{position:absolute;left:258px;top:12px;width:106px;height:23px;border-radius:12px;background:linear-gradient(#fff,#dcdcdc);border:1px solid #bbb;font-size:11px;font-weight:700;color:#555;text-align:center;line-height:21px}
.news .field{position:absolute;left:366px;top:8px;width:330px;height:32px;background:linear-gradient(#fff,#eef0ee);border:1px solid #ddd;font-size:9px;font-style:italic;color:#999;padding:9px 12px}
.news .go{position:absolute;right:8px;top:9px;width:48px;height:30px;font-size:11px;font-weight:700;color:#666;text-align:center;line-height:30px;border-left:1px solid #ddd}
.badge{top:1112px;background:#1f2f7a}
.social{top:1125px;width:26px;height:26px;border-radius:50%;background:#7b7b7b}
.profile{left:742px;top:1106px;font-size:10px;color:#333}
.pnet{left:752px;top:1127px;font-size:21px;font-weight:700;color:#111;letter-spacing:-.5px}
.copy{left:630px;top:1166px;font-size:10px;color:#333;letter-spacing:-.2px}
</style>
</head>
<body>
<div class="abs logo"><div class="name">Fenwold Electrical</div><div class="sub">SERVICES LIMITED</div></div>
<nav class="abs nav"><a class="active">Home</a><a>Services</a><a>Clients</a><a>Responsabilities</a><a>Contact Us</a></nav>

<div class="abs grey-band"></div>
<div class="abs hero" role="img" aria-label="Electrician in a blue cap wiring an industrial distribution board"></div>
<div class="abs arrow left"><svg width="54" height="86"><polyline points="32,34 22,43 32,52" fill="none" stroke="#333" stroke-width="4"/></svg></div>
<div class="abs arrow right"><svg width="54" height="86"><polyline points="24,34 34,43 24,52" fill="none" stroke="#333" stroke-width="4"/></svg></div>
<div class="abs caption"><h2><span>Electrical</span> Installation</h2><p><b>✣</b> Commercial <b>✣</b> Industrial <b>✣</b> Domestic</p></div>

<h3 class="abs sec-title" style="left:72px;top:451px">About Us</h3>
<h3 class="abs sec-title" style="left:567px;top:451px">Services</h3>
<div class="abs photo" style="left:74px;top:490px;width:448px;height:157px" role="img" aria-label="Row of industrial switchgear panels with red isolator switches"></div>
<div class="abs photo" style="left:566px;top:490px;width:277px;height:157px;background:linear-gradient(135deg,#8e8f8e,#c6c2bb 50%,#5f5f5f)" role="img" aria-label="Hand wiring terminal blocks in an electrical cabinet"></div>

<p class="abs lead"><span>Established in 2005 Fenwold Electrical Services Limited</span> is an independent company that has grown steadily over that period into a respected Commercial and Domestic Electrical installer providing it's services nationwide.</p>
<p class="abs body-text" style="left:72px;top:731px;width:450px">Professional and reliable, the secret of our success has come from recommendations from our customer base. Our staffing levels allow us to be flexible enough to tackle any size of project, contracts often exceeding 100K, yet we are able to complete the more modest budget competitively.</p>
<p class="abs body-text" style="left:566px;top:659px;width:281px;text-align:justify;line-height:14px">We provide a range of services covering design, installation, maintenance and testing. All our elecrical engineers are employed by us. This ensures we can sully a reliable and trusted service that service the following sectors:</p>
<ul class="abs list"><li>• Electrical Installation</li><li>• Data Network Cabling &amp; Systems</li><li>• Fire Alarm Systems</li></ul>
<span class="abs read" style="left:447px;top:800px">READ MORE &gt;&gt;</span>
<span class="abs read" style="left:772px;top:800px">READ MORE &gt;&gt;</span>

<div class="abs band"></div>
<h3 class="abs overview">Overview</h3>
<div class="abs tile" style="left:72px"><div class="photo" style="width:100%;height:100%;background:linear-gradient(135deg,#e8e8e4,#a9a59c)" role="img" aria-label="Food factory worker at a processing line"></div><span class="label">FOOD INDUSTRY</span></div>
<div class="abs tile" style="left:277px"><div class="photo" style="width:100%;height:100%;background:linear-gradient(135deg,#6a4a22,#d9a54a 50%,#5a3a18)" role="img" aria-label="Lit shopping centre with retail units"></div><span class="label">RETAIL PREMISES</span></div>
<div class="abs tile" style="left:480px"><div class="photo" style="width:100%;height:100%;background:linear-gradient(135deg,#d8dde2,#8c96a2)" role="img" aria-label="Office meeting in front of a chart on screen"></div><span class="label">COUNCILS</span></div>
<div class="abs tile" style="left:687px"><div class="photo" style="width:100%;height:100%;background:linear-gradient(#e9e4da,#9a4a3a)" role="img" aria-label="Empty classroom with desks and chalkboard"></div><span class="label">SCHOOLS<br>&amp; COLLEGES</span></div>

<div class="abs news">
  <span class="title">E-Mail Newsletter<small>To get updates to your mail</small></span>
  <span class="signin">SIGN IN</span>
  <span class="field">Enter your e-mail address<span class="go">GO</span></span>
</div>

<div class="abs badge" style="left:72px;width:62px;height:38px;border-radius:50%"></div>
<div class="abs badge" style="left:168px;width:76px;height:26px;top:1118px;background:var(--red)"></div>
<span class="abs profile">View Companies profile</span>
<span class="abs social" style="left:630px"></span>
<span class="abs social" style="left:663px"></span>
<span class="abs social" style="left:696px"></span>
<span class="abs pnet">ProfileNet</span>
<span class="abs copy">© 2012 fenwoldelectricalservices. All rights reserved.</span>
</body>
</html>
```